Revamp our wedding venue website

Currently we are using wordpress for our website and hoped to find a designer that can assist us with making the website prettier and more pleasing and draw more interest. www.velmorhall.net is our current site. We are connected to google business mail, so I would prefer to stay with this for now and update our gallery with new photos, blog page and putting the contact us form back on all the pages.

Target Market(s)

20-40 years of age, all ranges of styles and generally clients looking for a different modern feel vs. a hotel hall.

Industry/Entity Type

Wedding

Logo Text

1947 Velmor Hall

Number of Pages Required

4 page

Font styles to use
Serif

Requirements
Must have
• Light, airy feel. Romantic and informative. Mobile friendly and easy to contact us-preferred contact form on all pages. Gallery of photos. Previous reviews
Nice to have
• Bio of staff, maybe some videos, and fun things to do in the area for out of town guests. Maps and also venue blank floor plan.

```html
<!DOCTYPE html>
<html lang="en">
<head>
<meta charset="utf-8">
<title>1947 Velmor Hall — Weddings &amp; Events</title>
<link href="https://fonts.googleapis.com/css2?family=Pinyon+Script&family=Arimo:wght@400&family=Roboto:ital,wght@1,300&display=swap" rel="stylesheet">
<style>
:root{
  --ink:#1c1c1c;
  --text:#2a2a2a;
  --muted:#6b6b6b;
  --brand:#4a4a4a;
  --white:#ffffff;
  --band-grey:#efefef;
  --frame:#d6d6d6;
}
*{margin:0;padding:0;box-sizing:border-box}
html,body{width:1200px;height:3220px;overflow:hidden;background:var(--white)}
body{position:relative;font-family:"Arimo",Arial,sans-serif;color:var(--text)}
.script{font-family:"Pinyon Script",cursive;font-weight:400}
.abs{position:absolute}

/* hero */
.hero{left:0;top:0;width:1200px;height:676px;
  background:linear-gradient(180deg,#e3eef5 0%,#d4e4ee 44%,#4f86a4 52%,#3e7895 62%,#8aa9b5 66%,#a5784e 72%,#8a5f3c 88%,#c59a6f 100%)}
.brand{left:0;top:18px;width:1200px;text-align:center;font-family:"Arimo",Arial,sans-serif;font-weight:400;font-size:24px;line-height:32px;letter-spacing:1px;color:var(--brand)}
.nav{left:0;top:116px;width:1200px;display:flex;justify-content:center;gap:31px;font-size:17px;letter-spacing:.2px;color:var(--ink)}

/* intro */
.intro-title{left:0;top:766px;width:1200px;text-align:center;font-size:46px;color:var(--ink)}
.intro-sub{left:0;top:836px;width:1200px;text-align:center;font-size:21px;line-height:24px;color:var(--muted)}
.intro-body{left:118px;top:928px;width:964px;text-align:center;font-size:17px;line-height:25px;color:var(--text)}
.quote{left:110px;top:1088px;width:980px;text-align:center;font-family:"Roboto",Arial,sans-serif;font-style:italic;font-weight:300;font-size:26px;line-height:34px;color:var(--muted)}
.quote-by{left:0;top:1168px;width:1200px;text-align:center;font-size:17px;color:var(--text)}

/* gallery */
.gallery{left:0;top:1288px;width:1200px;height:677px;background:linear-gradient(135deg,#e4e4e4,#d2d2d2 50%,#e6e6e6)}
.section-label{left:0;width:1200px;text-align:center;font-size:30px;color:var(--ink)}
.gallery-grid{left:120px;top:1385px;width:958px;height:541px;display:grid;grid-template-columns:repeat(3,1fr);grid-template-rows:repeat(2,1fr);gap:7px}
.photo{width:100%;height:100%}

/* info */
.info-band{left:0;top:1965px;width:1200px;height:504px;background:var(--band-grey)}
.info-card{left:122px;top:2040px;width:956px;height:350px;background:var(--white);box-shadow:0 2px 6px rgba(0,0,0,.08)}
.info-col{text-align:center;font-size:15.5px;line-height:22px;color:var(--ink)}
.info-col h3{font-family:"Pinyon Script",cursive;font-weight:400;font-size:29px;margin-bottom:26px}
.video{left:419px;top:2130px;width:360px;height:210px;background:linear-gradient(180deg,#cfe0c7 0%,#8fb07c 40%,#e08f74 62%,#3a3a3a 78%,#9aa48a 100%)}
.video-bar{left:419px;top:2316px;width:360px;height:24px;background:rgba(20,20,20,.75)}

/* reviews */
.reviews{left:0;top:2469px;width:1200px;height:676px;background:linear-gradient(180deg,#7e9a63 0%,#5f7b48 30%,#8d8f80 60%,#b4aba0 100%)}
.notch{left:0;top:2469px}
.review{height:435px;top:2620px;background:var(--white);padding:14px}
.review-inner{width:100%;height:100%;border:2px solid var(--frame);padding:58px 22px 0;font-size:15.5px;line-height:24px;color:var(--ink);text-align:justify}
.review-inner h4{font-family:"Pinyon Script",cursive;font-weight:400;font-size:32px;line-height:36px;text-align:center;margin-bottom:40px}
.review-inner p+p{margin-top:24px}

.footer{left:0;top:3145px;width:1200px;height:75px;background:var(--white)}
.footer-name{left:0;top:3176px;width:1200px;text-align:center;font-family:"Arimo",Arial,sans-serif;font-size:20px;letter-spacing:1px;color:var(--brand)}
</style>
</head>
<body>

<header>
  <div class="abs hero" role="img" aria-label="Wedding party standing on coastal rocks looking out over the ocean"></div>
  <div class="abs brand">1947<br>Velmor Hall</div>
  <nav class="abs nav"><span>HOME</span><span>WEDDINGS</span><span>EVENTS</span><span>CATERING</span><span>GALLERY</span><span>CONTACT US</span></nav>
</header>

<section>
  <h1 class="abs intro-title script">Weddings &amp; Events at the 1947 Velmor Hall</h1>
  <p class="abs intro-sub">Imagine your wedding or event in Fairhaven’s premiere,<br>unique and historic venue</p>
  <p class="abs intro-body">When choosing the location for your wedding or event, the 1947 Velmor Hall provides you with an all-inclusive experience, from the moment you arrive, through the creative food, and amazing photo opportunities. The unique open-kitchen provides you, and your guests a front-row seat to our creative, and talented chefs, as they prepare a culinary experience like no other. The full, and spacious bar, serves up wonderful libations and specialty cocktails that enhance your experience.</p>
  <p class="abs quote">“It’s been almost a month since my wedding at the Velmor Hall and I am still with my<br>mouth open, it was absolutely beautiful.”</p>
  <p class="abs quote-by">– Marisol &amp; Theo, Fairhaven, FL</p>
</section>

<section>
  <div class="abs gallery" role="img" aria-label="Soft grey floral pattern background"></div>
  <h2 class="abs section-label script" style="top:1320px">Gallery</h2>
  <div class="abs gallery-grid">
    <div class="photo" role="img" aria-label="Pink and white floral centerpiece on a table" style="background:linear-gradient(135deg,#d98aa5,#f0e6e4 60%,#7fa07a)"></div>
    <div class="photo" role="img" aria-label="Bride and bridesmaids holding bouquets" style="background:linear-gradient(135deg,#a9b0a0,#ece6dc 50%,#9aa391)"></div>
    <div class="photo" role="img" aria-label="Outdoor reception tables under a vine arbor" style="background:linear-gradient(180deg,#5a6a3c,#8f9a6c 55%,#c9c2ae)"></div>
    <div class="photo" role="img" aria-label="Couple walking down a garden path between hedges" style="background:linear-gradient(180deg,#3f5a35,#5d7a4d 60%,#cfcbbf)"></div>
    <div class="photo" role="img" aria-label="White orchid bouquet held by the bride" style="background:linear-gradient(135deg,#3c3c48,#f2f1ea 55%,#6a8a55)"></div>
    <div class="photo" role="img" aria-label="Bride holding a blush and white bouquet" style="background:linear-gradient(135deg,#c9b8a8,#f3ede6 50%,#6f7c82)"></div>
  </div>
</section>

<section>
  <div class="abs info-band"></div>
  <div class="abs info-card"></div>
  <div class="abs info-col" style="left:150px;top:2070px;width:240px">
    <h3>Contact Us</h3>
    <p>Have questions? Want to come and see the 1947 Velmor Hall for yourselves? Call or contact our wedding and event specialists now:</p>
    <p style="margin-top:22px">events@velmorhall.net<br>555.214.0187</p>
  </div>
  <div class="abs info-col" style="left:419px;top:2070px;width:360px"><h3>Video</h3></div>
  <div class="abs video" role="img" aria-label="Video still of the wedding party lined up on a lawn"></div>
  <div class="abs video-bar"></div>
  <svg class="abs" style="left:426px;top:2320px" width="350" height="16" viewBox="0 0 350 16">
    <polygon points="2,3 11,8 2,13" fill="#fff"/>
    <rect x="20" y="7" width="260" height="2" fill="#888"/>
    <rect x="20" y="7" width="40" height="2" fill="#fff"/>
    <rect x="300" y="4" width="12" height="8" fill="none" stroke="#fff" stroke-width="1.5"/>
    <rect x="324" y="4" width="12" height="8" fill="none" stroke="#fff" stroke-width="1.5"/>
  </svg>
  <div class="abs info-col" style="left:815px;top:2070px;width:240px">
    <h3>Visit Us</h3>
    <p>We’re conveniently located in historic Old Harbor at:</p>
    <p style="margin-top:22px">1947 East Larkin Ave.<br>Fairhaven, FL 33999</p>
  </div>
</section>

<section>
  <div class="abs reviews" role="img" aria-label="Guests gathered at an outdoor garden reception under trees"></div>
  <svg class="abs notch" width="1200" height="100" viewBox="0 0 1200 100"><polygon points="440,0 762,0 601,97" fill="#efefef"/></svg>
  <h2 class="abs section-label script" style="top:2482px;font-size:26px">Reviews</h2>
  <article class="abs review" style="left:122px;width:314px"><div class="review-inner"><h4>Evelina</h4><p>1947 Velmor Hall was an absolute dream! Everything was right - the space, the food, the budget. They made planning our wedding easy, and we are so thankful to them! Thank you so much to the staff at 1947 Velmor Hall.</p></div></article>
  <article class="abs review" style="left:459px;width:282px"><div class="review-inner"><h4>Nora &amp; Pete</h4><p>1947 Velmor Hall was an absolute dream! Everything was right - the space, the food, the budget.</p><p>They made planning our wedding easy, and we are so thankful to them!</p></div></article>
  <article class="abs review" style="left:797px;width:276px"><div class="review-inner"><h4>Ivy &amp; Sam</h4><p>1947 Velmor Hall was an absolute dream!</p><p>Everything was right - the space, the food, the budget. They made planning our wedding easy, and we are so thankful to them!</p></div></article>
</section>

<footer>
  <div class="abs footer"></div>
  <div class="abs footer-name">1947 Velmor Hall</div>
</footer>

</body>
</html>
```